Custom Publisher Theme Needed

We need a custom Publisher theme built with the following features:

1. Flat style design
2. Fully responsive - built for mobile and tablets first; bootstrap or other framework used
3. Flexible - comes with homepage layouts for portfolios, agencies, and magazines
4. Built in 'contact' and 'about us' styling
5. Pre-populated pages and content, including reusable images
6. Multiple slider options

We are completely open to your creativity as far as the overall design style is concerned, but some of our favorites are:
http://themes.plovarek.com/themeselector/?theme=TideBoard
http://www.gorvelta.ru/levelpress/
http://layoutquarry.com/wp/vesk/intro/
http://theme.brindolaq.net/second/

Most unique and in-depth style wins!

Reason: We need more designs!

Reason: Waiting on final submissions and revisions. Thanks!

```html
<!DOCTYPE html>
<html lang="en">
<head>
<meta charset="utf-8">
<title>Company Theme – Home</title>
<link rel="stylesheet" href="https://fonts.googleapis.com/css2?family=Raleway:wght@400;500;600&family=Open+Sans:wght@400;600;700&family=Noto+Serif:ital@1&display=swap">
<style>
:root{
  --teal:#1ea5b8;
  --teal-dark:#178a9a;
  --ink:#333;
  --muted:#8a8a8a;
  --soft:#ebebed;
  --nav:#ececec;
  --dark:#1a1714;
  --footer:#484848;
  --footer-deep:#3b3b3b;
  --white:#fff;
}
*{box-sizing:border-box;margin:0;padding:0}
html,body{width:1200px;height:3799px;overflow:hidden}
body{position:relative;font-family:"Open Sans",Arial,sans-serif;color:var(--ink);background:var(--white)}
.abs{position:absolute}
.raleway{font-family:"Raleway",Arial,sans-serif}

/* header */
.site-header{left:0;top:0;width:1200px;height:95px;background:#fff}
.logo{left:120px;top:26px;font-family:"Raleway",sans-serif;font-size:24px;color:#444}
.social{left:757px;top:27px;display:flex;gap:6px}
.social span{width:27px;height:27px;border-radius:50%;background:var(--teal);display:block}

.main-nav{left:0;top:95px;width:1200px;height:47px;background:linear-gradient(#f4f4f4,#e2e2e2);border-top:1px solid #ddd;border-bottom:1px solid #d4d4d4}
.main-nav ul{list-style:none;display:flex;gap:34px;position:absolute;left:137px;top:14px;font-size:13px;color:#555}
.main-nav li.current{color:var(--teal);border-bottom:2px solid var(--teal);padding-bottom:10px}

/* slider */
.hero{left:0;top:142px;width:1200px;height:374px;background:radial-gradient(ellipse 260px 140px at 500px 30px,#f5e2b4 0%,#8a6a3a 20%,rgba(30,25,20,0) 60%),radial-gradient(ellipse 520px 420px at 760px 330px,#3d3a3a 0%,#141313 70%),#0d0c0c}
.hero-caption{left:130px;top:120px}
.hero-caption h2{display:inline-block;background:rgba(0,0,0,.55);color:#eee;font-family:"Raleway",sans-serif;font-weight:400;font-size:27px;padding:4px 10px}
.hero-caption p{margin-top:8px;background:rgba(0,0,0,.5);color:#ddd;font-size:13px;line-height:19px;padding:6px 10px;width:330px;text-transform:uppercase}
.arrow{top:166px;width:28px;height:34px;background:rgba(255,255,255,.25)}
.dots{display:flex;gap:6px}
.dots span{width:11px;height:11px;border-radius:50%;background:#bbb;display:block}
.dots span.on{background:var(--teal)}

/* intro */
.intro{left:0;top:516px;width:1200px;height:412px;background:#fff}
.intro-shadow{left:0;top:40px;width:1200px;height:10px;background:linear-gradient(#e4e4e4,#fff)}
.intro h1{left:120px;top:98px;font-family:"Raleway",sans-serif;font-weight:400;font-size:31px;color:#333}
.intro h1 em{font-style:normal;color:var(--teal)}
.intro p{left:120px;top:154px;width:320px;font-size:12.5px;line-height:19px;color:#666}
.intro p a{color:var(--teal);text-decoration:none}
.btn{background:var(--teal);color:#fff;font-size:12px;font-weight:600;display:flex;align-items:center;justify-content:center}
.devices{left:585px;top:100px;width:475px;height:312px;background:linear-gradient(160deg,#e4e4e4,#b9b9b9 60%,#fff);border-radius:4px}

/* features */
.features{left:0;top:928px;width:1200px;height:452px;background:var(--soft)}
.feature{top:120px;width:300px;text-align:center}
.feature .icon{width:117px;height:117px;border-radius:50%;background:#c9c9cb;margin:0 auto}
.feature h3{font-family:"Raleway",sans-serif;font-weight:400;font-size:23px;color:#333;margin-top:34px}
.feature p{font-size:11.5px;line-height:17px;color:#888;margin-top:10px}

/* experts */
.experts{left:0;top:1380px;width:1200px;height:567px;background:radial-gradient(ellipse 420px 260px at 380px 560px,#8a5f2c 0%,rgba(60,40,20,.4) 50%,rgba(0,0,0,0) 80%),radial-gradient(ellipse 400px 300px at 300px 60px,#3a332c 0%,rgba(0,0,0,0) 70%),var(--dark)}
.experts h2{left:120px;top:122px;font-family:"Raleway",sans-serif;font-weight:400;font-size:32px;line-height:40px;color:#fff}
.experts p{left:120px;top:218px;width:320px;font-size:12.5px;line-height:19px;color:#ccc}
.experts .byline{left:120px;top:320px;font-size:12.5px;color:#ccc}
.experts .byline b{color:var(--teal);font-weight:400}
.posters{left:560px;top:70px;width:490px;height:360px;background:linear-gradient(120deg,#d6d6d6 0%,#c23a3a 35%,#9fb7c4 60%,#3c4e5c 100%);opacity:.9}

/* section titles */
.section-head{width:1200px;text-align:center}
.mark{width:20px;height:14px;margin:0 auto}
.section-head h2{font-family:"Raleway",sans-serif;font-weight:400;font-size:32px;color:#333;margin-top:28px}
.section-head .rule{width:95px;height:1px;background:#ccc;margin:18px auto 0}
.section-head p{width:720px;margin:16px auto 0;font-size:12px;line-height:18px;color:#888}

/* work grid */
.work{left:0;top:1947px;width:1200px;height:643px}
.tile{width:222px;height:163px;display:flex;align-items:center;justify-content:center;font-family:"Raleway",sans-serif;font-weight:600;font-size:26px}

/* testimonial */
.testimonial{left:0;top:2590px;width:1200px;height:386px;background:radial-gradient(ellipse 300px 220px at 1000px 150px,#5a5a58 0%,rgba(0,0,0,0) 70%),linear-gradient(90deg,#232425,#3b3c3d 60%,#4a4b4c)}
.quote-mark{left:0;width:1200px;top:62px;text-align:center;font-family:"Noto Serif",serif;font-size:64px;color:var(--teal);line-height:1}
.testimonial blockquote{left:175px;top:142px;width:860px;font-family:"Noto Serif",serif;font-style:italic;font-size:19.5px;line-height:29px;color:#fff}
.testimonial cite{left:175px;top:262px;font-style:normal;font-size:13px;letter-spacing:.5px;color:#aaa;border-left:3px solid var(--teal);padding-left:8px}

/* clients */
.clients{left:0;top:2976px;width:1200px;height:396px}
.client{top:282px;font-size:19px;font-weight:700;color:#555}

/* cta */
.cta{left:0;top:3372px;width:1200px;height:104px;background:#e8e8e8}
.cta h3{left:198px;top:34px;font-family:"Raleway",sans-serif;font-weight:500;font-size:27px;color:#333}

/* footer */
.footer{left:0;top:3476px;width:1200px;height:260px;background:var(--footer)}
.fcol{top:40px;width:300px}
.fcol h4{font-family:"Raleway",sans-serif;font-weight:400;font-size:19px;color:#fff;padding-bottom:10px;border-bottom:1px solid #5d5d5d}
.fcol ul{list-style:none;margin-top:10px;font-size:11.5px;line-height:22px;color:#bbb}
.fcol ul li::before{content:"› ";color:#999}
.contact li{display:flex;gap:10px;align-items:flex-start;font-size:11.5px;line-height:17px;color:#bbb;margin-bottom:12px}
.contact li::before{content:none}
.squares{display:flex;flex-wrap:wrap;gap:5px;margin-top:18px;width:240px}
.squares span{width:27px;height:27px;background:#5e5e5e;display:block}
.bottom-bar{left:0;top:3736px;width:1200px;height:63px;background:var(--footer-deep)}
.bottom-social{left:120px;top:20px;display:flex;gap:6px}
.bottom-social span{width:23px;height:23px;border-radius:50%;background:#6a6a6a;display:block}
.copyright{left:760px;top:24px;font-size:11px;color:#999}
.copyright b{font-weight:400;color:var(--teal)}
</style>
</head>
<body>

<header class="site-header abs">
  <div class="logo abs">Company Logo</div>
  <div class="social abs"><span></span><span></span><span></span><span></span><span></span><span></span><span></span><span></span><span></span><span></span></div>
</header>

<nav class="main-nav abs">
  <ul>
    <li class="current">Home</li><li>Page</li><li>Blog</li><li>Contact Us</li><li>Shortcodes</li><li>Ajax Portfolio 3 Columns</li><li>Ajax Portfolio 4 Columns</li>
  </ul>
</nav>

<section class="hero abs" role="img" aria-label="Slider photo of a planet in deep space with a bright sunrise glow">
  <div class="hero-caption abs">
    <h2>Lorem ipsum</h2>
    <p>Lorem ipsum is simply dummy text of the printing and typesetting industry.</p>
  </div>
  <div class="arrow abs" style="left:0"><svg width="28" height="34"><path d="M17 11l-6 6 6 6" stroke="#fff" stroke-width="2" fill="none"/></svg></div>
  <div class="arrow abs" style="right:0"><svg width="28" height="34"><path d="M11 11l6 6-6 6" stroke="#fff" stroke-width="2" fill="none"/></svg></div>
  <div class="dots abs" style="left:566px;top:352px"><span class="on" style="background:#ddd"></span><span></span><span></span></div>
</section>

<section class="intro abs">
  <div class="intro-shadow abs"></div>
  <h1 class="abs">LOREM <em>IPSUM</em></h1>
  <p class="abs">Lorem ipsum dolor sit amet, consectetuer adipiscing elit, sed diam nonummy nibh euismod tincidunt ut laoreet dolore magna aliquam erat volutpat. <a>Web and Graphic Design.</a></p>
  <div class="btn abs" style="left:120px;top:252px;width:236px;height:42px">See work we do for our clients &#9656;</div>
  <div class="devices abs" role="img" aria-label="Desktop monitor and tablet showing a team photo and the theme"></div>
</section>

<section class="features abs">
  <div class="feature abs" style="left:115px">
    <div class="icon"><svg width="117" height="117"><ellipse cx="58" cy="60" rx="22" ry="17" fill="#fff"/><rect x="52" y="38" width="12" height="6" fill="#fff"/><rect x="46" y="74" width="6" height="10" fill="#fff"/><rect x="64" y="74" width="6" height="10" fill="#fff"/></svg></div>
    <h3>People</h3>
    <p>Duis aute irure dolor in reprehenderit in voluptate velit esse cillum dolore eu fugiat nulla pariatur. Sed ut perspiciatis unde omnis iste natus error sit.</p>
  </div>
  <div class="feature abs" style="left:448px">
    <div class="icon"><svg width="117" height="117"><rect x="38" y="48" width="18" height="32" fill="#fff"/><rect x="60" y="38" width="18" height="42" fill="#fff"/><rect x="63" y="44" width="4" height="4" fill="#c9c9cb"/><rect x="70" y="44" width="4" height="4" fill="#c9c9cb"/></svg></div>
    <h3>Engineering</h3>
    <p>Ut wisi enim ad minim veniam, quis nostrud exerci tation ullamcorper suscipit lobortis nisl ut aliquip ex ea commodo consequat duis autem vel eum iriure.</p>
  </div>
  <div class="feature abs" style="left:780px">
    <div class="icon"><svg width="117" height="117"><path d="M40 78l26-26 6 6-26 26z" fill="#fff"/><path d="M68 44l10-8 6 6-8 10z" fill="#fff"/></svg></div>
    <h3>Creative</h3>
    <p>Ut enim ad minim veniam, quis nostrud exercitation ullamco laboris nisi ut aliquip ex ea commodo consequat. Nam liber tempor cum soluta nobis.</p>
  </div>
</section>

<section class="experts abs">
  <h2 class="abs">Web and Graphic<br>Design Experts</h2>
  <p class="abs">Consectetur sitae eleifend ac, enim. Aliquam lorem ante, dapibus in, viverra quis, feugiat a, tellus. Phasellus viverra nulla ut metus varius laoreet. Quisque rutrum aenean.</p>
  <div class="byline abs">Posted by <b>Dorian Vale</b></div>
  <div class="btn abs" style="left:120px;top:350px;width:232px;height:44px">Meet our design and dev team &#9656;</div>
  <div class="posters abs" role="img" aria-label="Two tilted printed posters, one with a red car and one with a city skyline"></div>
</section>

<section class="work abs">
  <div class="section-head abs" style="top:20px">
    <svg class="mark" viewBox="0 0 20 14"><circle cx="10" cy="3" r="3" fill="#1ea5b8"/><circle cx="4" cy="11" r="3" fill="#1ea5b8"/><circle cx="16" cy="11" r="3" fill="#1ea5b8"/></svg>
    <h2>Some of our Recent Work</h2>
    <div class="rule"></div>
    <p>Stet clita kasd gubergren, no sea takimata sanctus est lorem ipsum dolor sit amet. Lorem ipsum dolor sit amet, consetetur sadipscing elitr, sed diam nonumy eirmod tempor invidunt ut labore et dolore magna aliquyam erat, sed diam voluptua at vero eos et accusam justo duo dolores.</p>
  </div>
  <div class="tile abs" style="left:120px;top:247px;background:#f6c514;color:#222">Tarnlo</div>
  <div class="tile abs" style="left:358px;top:247px;background:#e2493f;color:#fff">Velwick</div>
  <div class="tile abs" style="left:595px;top:247px;background:#a8dcf0;color:#1f3552">Lexa Hall</div>
  <div class="tile abs" style="left:833px;top:247px;background:#e0262b;color:#fff">Arvent</div>
  <div class="tile abs" style="left:120px;top:434px;background:#1d2b3d;color:#fff">Sonaro</div>
  <div class="tile abs" style="left:358px;top:434px;background:linear-gradient(#f3f3f3,#ddd)" role="img" aria-label="Illustration of a brick townhouse"></div>
  <div class="tile abs" style="left:595px;top:434px;background:#fff;color:#f29a1e;border:1px solid #eee">Oruvia</div>
  <div class="tile abs" style="left:833px;top:434px;background:#fdeaf0;color:#222">Mirella</div>
</section>

<section class="testimonial abs" role="img" aria-label="Blurred desk photo with a notebook, pen and phone">
  <div class="quote-mark abs">&#8220;</div>
  <blockquote class="abs">Lorem ipsum dolor sit amet, consetetur sadipscing elitr, sed diam nonumy eirmod tempor invidunt ut labore et dolore sit amet. Ut enim ad minim veniam, quis nostrud exercitation ullamco laboris nisi ut aliquid ex ea commodi consequat duis autem.</blockquote>
  <cite class="abs">ELIAS MARROW, CEO, NORTHWIND PARTNERS</cite>
  <div class="dots abs" style="left:568px;top:320px"><span></span><span></span><span class="on"></span></div>
</section>

<section class="clients abs">
  <div class="section-head abs" style="top:30px">
    <svg class="mark" viewBox="0 0 20 14"><circle cx="10" cy="3" r="3" fill="#1ea5b8"/><circle cx="4" cy="11" r="3" fill="#1ea5b8"/><circle cx="16" cy="11" r="3" fill="#1ea5b8"/></svg>
    <h2>Some of the Clients we have handled</h2>
    <div class="rule"></div>
    <p>Stet clita kasd gubergren, no sea takimata sanctus est lorem ipsum dolor sit amet. Lorem ipsum dolor sit amet, consetetur sadipscing elitr, sed diam nonumy eirmod tempor invidunt ut labore et dolore magna aliquyam erat, sed diam voluptua at vero eos et accusam justo.</p>
  </div>
  <div class="client abs" style="left:136px">Dumorel</div>
  <div class="client abs" style="left:312px">Tidyo</div>
  <div class="client abs" style="left:472px">Smarvex</div>
  <div class="client abs" style="left:624px">Lumora</div>
  <div class="client abs" style="left:796px">Banfeld</div>
  <div class="client abs" style="left:976px">Kelric</div>
</section>

<section class="cta abs">
  <h3 class="abs">Ready to talk about your project?</h3>
  <div class="btn abs" style="left:783px;top:30px;width:152px;height:45px;font-size:13px">Contact Us Now</div>
</section>

<footer class="footer abs">
  <div class="fcol abs" style="left:120px">
    <h4>Meta</h4>
    <ul><li>Log in</li><li>Entries RSS</li><li>Comments RSS</li><li>Publisher.org</li></ul>
  </div>
  <div class="fcol abs" style="left:450px">
    <h4>Contact Info</h4>
    <ul class="contact">
      <li><svg width="12" height="16"><path d="M6 1a5 5 0 015 5c0 4-5 9-5 9S1 10 1 6a5 5 0 015-5z" fill="#999"/></svg><span>Lakeview<br>North District</span></li>
      <li><svg width="12" height="14"><path d="M2 1h3l1 3-2 1a7 7 0 004 4l1-2 3 1v3a1 1 0 01-1 1A10 10 0 011 2a1 1 0 011-1z" fill="#999"/></svg><span>+00 555 012 3456</span></li>
      <li><svg width="12" height="12"><rect x="0" y="2" width="12" height="9" fill="#999"/><path d="M0 2l6 5 6-5" stroke="#484848" fill="none"/></svg><span>hello@northfold.com</span></li>
    </ul>
  </div>
  <div class="fcol abs" style="left:782px">
    <h4>Find us online</h4>
    <div class="squares"><span></span><span></span><span></span><span></span><span></span><span></span><span></span><span></span><span></span></div>
  </div>
</footer>

<div class="bottom-bar abs">
  <div class="bottom-social abs"><span></span><span></span><span></span><span></span><span></span><span></span><span></span><span></span><span></span><span></span><span></span></div>
  <div class="copyright abs">Copyright &copy; 2013 <b>Company Logo</b>. Powered by <b>Publisher</b> and <b>Northfold</b>.</div>
</div>

</body>
</html>
```